Trevik Builders Business Card Design Project

Clean sharp business card
Ability to write on back of card
Details for the card -
Address: PO Box 5087, Marrowdale, Qld, 4319
ABN: 47 305 921 276
BSA LIC 6825170
Ph: 07 4651 2839
Fax: 07 4651 2840
Email: trevikbuilders@quillpost.net

Reason: Time to review designs after weekend

```html
<!DOCTYPE html>
<html lang="en">
<head>
<meta charset="utf-8">
<title>Trevik Builders – Business Card Options</title>
<link rel="stylesheet" href="https://fonts.googleapis.com/css2?family=Arimo:wght@400;700&display=swap">
<style>
  :root {
    --sheet: #ffffff;
    --ink: #000000;
    --card-dark: #000000;
    --card-dark-soft: #0b0b0b;
    --card-light: #ffffff;
    --card-light-soft: #f3f3f3;
    --card-edge: #c8c8c8;
    --silver: #d4d4d6;
    --orange: #f39019;
  }
  * { box-sizing: border-box; margin: 0; padding: 0; }
  html, body {
    width: 1200px; height: 874px; overflow: hidden;
    background: var(--sheet);
    font-family: "Arimo", Arial, sans-serif;
    color: var(--ink);
  }
  .sheet { position: relative; width: 1200px; height: 874px; }

  .option-label {
    position: absolute; top: 60px; width: 469px;
    text-align: center; font-size: 24px; font-weight: 400; line-height: 28px;
  }
  .col-textured { left: 96px; }
  .col-plain { left: 632px; }

  .card {
    position: absolute; width: 469px; height: 310px; overflow: hidden;
  }
  .card-front { top: 107px; background: var(--card-dark); }
  .card-back {
    top: 464px; background: var(--card-light);
    border: 1px solid var(--card-edge);
  }
  .col-textured.card-front {
    background: radial-gradient(ellipse at 50% 45%, #141414 0%, var(--card-dark-soft) 55%, #050505 100%);
  }
  .col-textured.card-back .back-body {
    background: linear-gradient(180deg, var(--card-light) 0%, var(--card-light-soft) 100%);
  }

  .front-brand {
    position: absolute; left: 0; right: 0; top: 126px;
    display: flex; align-items: center; justify-content: center; gap: 14px;
  }
  .brand-dot {
    flex: none; width: 26px; height: 26px; border-radius: 50%; background: var(--orange);
  }
  .brand-name {
    font-size: 44px; font-weight: 700; line-height: 52px; color: var(--silver); white-space: nowrap;
  }

  .back-band {
    position: absolute; left: 0; right: 0; height: 44px; background: var(--card-dark);
  }
  .band-top { top: 0; }
  .band-bottom { bottom: 0; display: flex; align-items: center; gap: 7px; padding-left: 12px; }
  .back-body { position: absolute; left: 0; right: 0; top: 44px; bottom: 44px; }
  .contact-list {
    position: absolute; left: 10px; top: 8px;
    list-style: none; font-size: 17px; line-height: 21px; white-space: nowrap;
  }
  .band-bottom .brand-dot { width: 12px; height: 12px; }
  .band-bottom .brand-name { font-size: 15px; line-height: 18px; }
</style>
</head>
<body>
<main class="sheet">
  <h2 class="option-label col-textured">Texturised</h2>
  <h2 class="option-label col-plain">Original</h2>

  <section class="card card-front col-textured" aria-label="Card front, textured">
    <div class="front-brand"><span class="brand-dot"></span><span class="brand-name">Trevik Builders</span></div>
  </section>
  <section class="card card-front col-plain" aria-label="Card front, plain">
    <div class="front-brand"><span class="brand-dot"></span><span class="brand-name">Trevik Builders</span></div>
  </section>

  <section class="card card-back col-textured" aria-label="Card back, textured">
    <div class="back-band band-top"></div>
    <div class="back-body">
      <ul class="contact-list">
        <li>Address: PO Box 5087, Marrowdale, Qld, 4319</li>
        <li>ABN: 47 305 921 276</li>
        <li>BAS LIC 6825170</li>
        <li>Ph: 46512839</li>
        <li>Fax: 46512840</li>
        <li>Email: trevikbuilders@quillpost.net</li>
      </ul>
    </div>
    <div class="back-band band-bottom"><span class="brand-dot"></span><span class="brand-name">Trevik Builders</span></div>
  </section>
  <section class="card card-back col-plain" aria-label="Card back, plain">
    <div class="back-band band-top"></div>
    <div class="back-body">
      <ul class="contact-list">
        <li>Address: PO Box 5087, Marrowdale, Qld, 4319</li>
        <li>ABN: 47 305 921 276</li>
        <li>BAS LIC 6825170</li>
        <li>Ph: 46512839</li>
        <li>Fax: 46512840</li>
        <li>Email: trevikbuilders@quillpost.net</li>
      </ul>
    </div>
    <div class="back-band band-bottom"><span class="brand-dot"></span><span class="brand-name">Trevik Builders</span></div>
  </section>
</main>
</body>
</html>
```